Letterhead and Stationary for Construction Company

Brisk Current needs modern Letterhead, Envelopes and Notepad designs.

Industry/Entity Type

Construction

Colors
f78f20
34a7d8
ffffff

Requirements
Must have
• Modern looking design.

```html
<!DOCTYPE html>
<html lang="en">
<head>
<meta charset="utf-8">
<title>Brisk Current Stationery</title>
<link href="https://fonts.googleapis.com/css2?family=Source+Sans+3:wght@400;600;700&display=swap" rel="stylesheet">
<style>
:root{
  --bg:#bbbcbe;
  --paper:#ffffff;
  --paper-soft:#f4f4f5;
  --orange:#f07a2a;
  --blue:#2470c2;
  --ink:#333333;
  --muted:#666666;
}
*{margin:0;padding:0;box-sizing:border-box}
html,body{width:1200px;height:1200px;overflow:hidden;background:var(--bg);font-family:"Source Sans 3",Arial,sans-serif;color:var(--ink)}
.sheet{position:absolute;background:var(--paper)}
.bands{position:absolute;left:0;right:0;bottom:0;height:11px}
.bands::before{content:"";position:absolute;left:0;right:0;top:0;height:4px;background:var(--blue)}
.bands::after{content:"";position:absolute;left:0;right:0;bottom:0;height:4px;background:var(--orange)}
.brand{position:absolute;display:flex;align-items:center;gap:6px;font-weight:700;color:var(--blue);white-space:nowrap;line-height:1}
.brand .dot{border-radius:50%;background:var(--orange);flex:none}
.flap{position:absolute;left:0;right:0;top:0;background:var(--orange);clip-path:polygon(0 0,100% 0,98% 100%,2% 100%);display:flex;align-items:center;justify-content:center;color:#fff;font-weight:700;letter-spacing:.5px}
.contact{position:absolute;font-size:6.5px;line-height:9px;color:var(--ink)}
.pad-bg{background:var(--paper-soft)}
.rings{position:absolute;display:flex}
.ring{background:var(--orange);border-radius:2px}
.letter-body p{font-size:5px;line-height:6.9px;color:var(--muted);margin-bottom:8px;text-align:justify}
</style>
</head>
<body>

<!-- Large envelope -->
<section class="sheet envelope-large" style="left:46px;top:74px;width:357px;height:506px">
  <div class="flap" style="height:60px;font-size:15px">Brisk Current</div>
  <div class="contact" style="left:36px;top:451px">555-018-246<br>48 Harbor Rd. Tampa, FL 33602<br>www.briskcurrent.com</div>
</section>

<!-- Letterhead -->
<section class="sheet letterhead" style="left:446px;top:75px;width:355px;height:503px">
  <div class="brand" style="left:37px;top:40px;font-size:17px"><span class="dot" style="width:18px;height:18px"></span>Brisk Current</div>
  <div class="contact" style="left:44px;top:79px">48 Harbor Rd. Tampa, FL 33602</div>
  <div class="bands"></div>
</section>

<!-- Top notepad -->
<section class="sheet notepad pad-bg" style="left:848px;top:128px;width:280px;height:387px">
  <div class="rings" style="left:18px;top:-6px;gap:9.3px">
    <span class="ring" style="width:4px;height:24px"></span><span class="ring" style="width:4px;height:24px"></span><span class="ring" style="width:4px;height:24px"></span><span class="ring" style="width:4px;height:24px"></span><span class="ring" style="width:4px;height:24px"></span><span class="ring" style="width:4px;height:24px"></span><span class="ring" style="width:4px;height:24px"></span><span class="ring" style="width:4px;height:24px"></span><span class="ring" style="width:4px;height:24px"></span><span class="ring" style="width:4px;height:24px"></span><span class="ring" style="width:4px;height:24px"></span><span class="ring" style="width:4px;height:24px"></span><span class="ring" style="width:4px;height:24px"></span><span class="ring" style="width:4px;height:24px"></span><span class="ring" style="width:4px;height:24px"></span><span class="ring" style="width:4px;height:24px"></span><span class="ring" style="width:4px;height:24px"></span><span class="ring" style="width:4px;height:24px"></span>
  </div>
  <div class="brand" style="left:0;right:0;top:200px;justify-content:center;font-size:24px"><span class="dot" style="width:22px;height:22px"></span>Brisk Current</div>
  <div class="contact" style="left:0;right:0;top:366px;text-align:center;font-size:7px">www.briskcurrent.com</div>
</section>

<!-- Small envelope -->
<section class="sheet envelope-small" style="left:48px;top:654px;width:362px;height:181px;background:#f6f6f6">
  <div class="flap" style="height:58px;font-size:15px">Brisk Current</div>
</section>

<!-- DL envelope -->
<section class="sheet envelope-dl" style="left:45px;top:885px;width:367px;height:171px">
  <div class="brand" style="left:25px;top:26px;font-size:15px"><span class="dot" style="width:15px;height:15px"></span>Brisk Current</div>
  <div style="position:absolute;left:25px;top:93px;width:98px;height:49px;border-radius:8px;background:linear-gradient(120deg,#f07a2a,#f59a5a 55%,#ec6f22)"></div>
  <div class="contact" style="right:19px;top:120px;text-align:right">555-018-246<br>48 Harbor Rd. Tampa, FL 33602<br>www.briskcurrent.com</div>
  <div class="bands" style="bottom:10px"></div>
</section>

<!-- Letter -->
<section class="sheet letter" style="left:442px;top:606px;width:342px;height:485px">
  <div class="brand" style="left:0;right:0;top:52px;justify-content:center;font-size:17px"><span class="dot" style="width:16px;height:16px"></span>Brisk Current</div>
  <div class="contact" style="left:0;right:0;top:79px;text-align:center;font-size:6px">48 Harbor Rd. Tampa, FL 33602</div>
  <div style="position:absolute;left:49px;top:118px;font-size:5.5px;line-height:6px">
    <b>Dear, Mr________</b><br><span style="font-size:4px">Designation</span><br><b style="font-size:4px">COMPANY NAME</b>
  </div>
  <div class="letter-body" style="position:absolute;left:49px;top:150px;width:244px">
    <p>Thank you for considering our team for your upcoming building project. We plan, manage and deliver sites with care, keeping schedules clear and budgets honest from the first survey to the final handover and inspection of every finished structure.</p>
    <p>Our crews bring years of field work across homes, offices and public works. Each job starts with a full site review, a written plan and a named lead who keeps you informed about progress, safety checks and any change in scope or cost.</p>
    <p>We use sound materials, trusted suppliers and tested methods so that every wall, floor and roof stands up to weather and daily use. Quality checks happen at every stage, and our records stay open to you throughout the whole build.</p>
    <p>Please review the attached proposal and let us know a convenient time to meet. We would be glad to walk the site together, answer questions and shape a schedule that suits your needs and goals for the year ahead.</p>
  </div>
  <div style="position:absolute;right:54px;top:386px;text-align:right;font-size:7.5px;font-weight:700;line-height:8px">YOUR NAME<br><span style="font-size:5px;font-weight:400">Designation</span></div>
  <div style="position:absolute;left:205px;top:428px;width:84px;height:1px;background:var(--ink)"></div>
  <svg style="position:absolute;left:0;top:450px" width="342" height="24" viewBox="0 0 342 24">
    <g fill="none" stroke="#333" stroke-width="0.9">
      <path d="M65 2 q-2 0 -2 2 q2 4 5 5 q2 0 2 -2 l-1.5 -1.5"/>
      <rect x="180" y="2" width="7" height="5"/><path d="M180 2 l3.5 3 l3.5 -3"/>
      <circle cx="303" cy="4.5" r="3.5"/><path d="M299.5 4.5 h7 M303 1 v7"/>
    </g>
    <g font-family="Source Sans 3, sans-serif" font-size="6" fill="#333" text-anchor="middle">
      <text x="67" y="19">555-018-246</text><text x="183" y="19">info@briskcurrent.com</text><text x="303" y="19">www.briskcurrent.com</text>
    </g>
  </svg>
  <div class="bands"></div>
</section>

<!-- Spiral notebook -->
<section class="sheet notebook pad-bg" style="left:827px;top:608px;width:343px;height:486px">
  <div class="rings" style="left:-21px;top:28px;flex-direction:column;gap:22.5px">
    <span class="ring" style="width:40px;height:8px"></span><span class="ring" style="width:40px;height:8px"></span><span class="ring" style="width:40px;height:8px"></span><span class="ring" style="width:40px;height:8px"></span><span class="ring" style="width:40px;height:8px"></span><span class="ring" style="width:40px;height:8px"></span><span class="ring" style="width:40px;height:8px"></span><span class="ring" style="width:40px;height:8px"></span><span class="ring" style="width:40px;height:8px"></span><span class="ring" style="width:40px;height:8px"></span><span class="ring" style="width:40px;height:8px"></span><span class="ring" style="width:40px;height:8px"></span><span class="ring" style="width:40px;height:8px"></span><span class="ring" style="width:40px;height:8px"></span>
  </div>
  <div class="brand" style="left:192px;top:360px;font-size:20px"><span class="dot" style="width:20px;height:20px"></span>Brisk Current</div>
  <div class="contact" style="left:196px;top:412px">555-018-246<br>info@briskcurrent.com<br>48 Harbor Rd. Tampa, FL 33602<br>www.briskcurrent.com</div>
  <div class="bands"></div>
</section>

</body>
</html>
```